Marketing and Outreach Collateral Template Design

We are a nonprofit that works with schools to provide advocacy and recently created a series of "Stand Up Strong" materials surrounding LGBTQ young people in schools. (The Bright Hallways Youth Coalition, a project of Civic Wellness Board of Greater Lakeview, or CWBGL).We would like create a few items (wallet cards, magnets, postcards, etc.) that different bits of information on them, i.e. "top five things you need to know about [subject matter]" with our contact info and how to access the materials. We would provide raw files, copy, and a comprehensive list of the materials we are looking for to create. **What we need from you** would be a template for each of the 3-5 supplemental items that we want to build with copy language that we could manipulate in InDesign or Illustrator. We would like the templates to accompany the materials that already exist that were developed by one of our youth, but you would be able to make adjustments, offer ideas for polishing, etc. I've attached an example of one of our materials for your reference.

```html
<!DOCTYPE html>
<html lang="en">
<head>
<meta charset="utf-8">
<title>Bright Hallways Youth Coalition – Outreach Card</title>
<link href="https://fonts.googleapis.com/css2?family=Arimo:wght@400;700&display=swap" rel="stylesheet">
<style>
  :root {
    --white: #ffffff;
    --blue: #2a86c8;
    --blue-deep: #1f73b3;
    --brown: #5a2b22;
    --brown-light: #8a4b3e;
    --ink: #1a1a1a;
    --photo-green: #3f6b35;
    --photo-grey: #8d9197;
  }
  * { box-sizing: border-box; margin: 0; padding: 0; }
  html, body { width: 1200px; height: 805px; overflow: hidden; background: var(--white); }
  body { font-family: "Arimo", Arial, sans-serif; }
  .card { position: relative; width: 1200px; height: 805px; overflow: hidden; background: var(--white); }
  .card__shapes { position: absolute; inset: 0; }

  .brand { position: absolute; left: 36px; top: 160px; display: flex; align-items: center; gap: 14px; }
  .brand__mark { width: 44px; height: 44px; border-radius: 50%; background: var(--blue); flex: none; }
  .brand__name { color: var(--brown); font-weight: 700; line-height: 1.1; font-size: 34px; white-space: nowrap; }
  .brand__name small { display: block; font-size: 22px; }

  .headline { position: absolute; left: 52px; top: 318px; color: var(--blue-deep); font-weight: 700; font-size: 46px; letter-spacing: 0.5px; white-space: nowrap; }
  .intro { position: absolute; left: 36px; top: 390px; width: 420px; color: var(--ink); font-size: 28px; line-height: 38px; white-space: nowrap; }

  .contacts { position: absolute; left: 78px; top: 614px; list-style: none; }
  .contacts li { display: flex; align-items: center; gap: 35px; height: 50px; color: var(--white); font-size: 27px; white-space: nowrap; }
  .contacts svg { width: 40px; height: 40px; flex: none; }

  .phone { position: absolute; left: 589px; top: 640px; width: 541px; height: 124px; border-radius: 62px;
    background: linear-gradient(180deg, var(--brown-light), var(--brown));
    display: flex; align-items: center; justify-content: center; gap: 30px;
    color: var(--white); font-weight: 700; font-size: 46px; letter-spacing: 1px; }
  .phone svg { width: 50px; height: 50px; }
</style>
</head>
<body>
<main class="card">
  <svg class="card__shapes" viewBox="0 0 1200 805" xmlns="http://www.w3.org/2000/svg">
    <defs>
      <linearGradient id="photoTone" x1="0" y1="0" x2="0" y2="1">
        <stop offset="0" stop-color="#3f6b35"/>
        <stop offset="0.55" stop-color="#5c7d55"/>
        <stop offset="1" stop-color="#8d9197"/>
      </linearGradient>
    </defs>
    <path class="band-blue" d="M0 620 Q 320 575 640 655 L1200 620 V805 H0 Z" fill="var(--blue)"/>
    <path class="swoosh-brown" d="M0 540 Q 280 490 600 620 Q 280 540 0 600 Z" fill="var(--brown)"/>
    <ellipse class="ring-brown" cx="1040" cy="180" rx="595" ry="505" fill="none" stroke="var(--brown)" stroke-width="4"/>
    <ellipse class="ring-blue" cx="1040" cy="180" rx="578" ry="488" fill="var(--blue)"/>
    <ellipse class="photo" cx="1040" cy="180" rx="560" ry="470" fill="url(#photoTone)"
      role="img" aria-label="Group photo of smiling young volunteers in matching shirts jumping outdoors in front of trees"/>
  </svg>

  <div class="brand">
    <span class="brand__mark"></span>
    <p class="brand__name"><small>BRIGHT HALLWAYS</small>YOUTH COALITION</p>
  </div>

  <h1 class="headline">LOREM IPSUM</h1>
  <p class="intro">Lorem ipsum dolor sit amet,<br>consectetuer adipiscing elit,<br>sed diam nonummy nibh</p>

  <ul class="contacts">
    <li>
      <svg viewBox="0 0 40 40"><rect x="3" y="9" width="34" height="22" fill="var(--white)"/><path d="M3 9 L20 23 L37 9" fill="none" stroke="var(--blue)" stroke-width="2.5"/></svg>
      Lorem ipsum Lorem ipsum
    </li>
    <li>
      <svg viewBox="0 0 40 40" fill="none" stroke-width="2.5"><circle cx="20" cy="20" r="16" fill="var(--white)"/><g stroke="var(--blue)"><ellipse cx="20" cy="20" rx="7" ry="16"/><path d="M4 20 H36 M7 12 H33 M7 28 H33"/></g></svg>
      Lorem ipsum Lorem ipsum
    </li>
    <li>
      <svg viewBox="0 0 40 40"><path d="M20 38 C 10 25 7 20 7 15 A 13 13 0 0 1 33 15 C 33 20 30 25 20 38 Z" fill="var(--white)"/><circle cx="20" cy="15" r="5" fill="var(--blue)"/></svg>
      Lorem ipsum Lorem ipsum
    </li>
  </ul>

  <div class="phone">
    <svg viewBox="0 0 24 24"><path fill="var(--white)" d="M6.6 10.8a15.1 15.1 0 0 0 6.6 6.6l2.2-2.2a1 1 0 0 1 1-.25 11.4 11.4 0 0 0 3.6.57 1 1 0 0 1 1 1V20a1 1 0 0 1-1 1A17 17 0 0 1 3 4a1 1 0 0 1 1-1h3.5a1 1 0 0 1 1 1c0 1.25.2 2.45.57 3.570a1 1 0 0 1-.25 1z"/></svg>
    <span>012-345-6789</span>
  </div>
</main>
</body>
</html>
```